NURSING: RISING PAST THE SHADOWED SILL

Size of the book cover: 140 x 215 mms

I need a cover for the 30,000 word book I have just written. It is a positive take on what I think nursing is and what it needs to be in the future. It is also my story of being nursed and of being a nurse.

My dream is that nurses honor themselves; that they look to the future with confidence and intelligence and that care continues to be delivered with compassionate person centeredness.

I define nursing as a professional workforce which, with probity, prevent or relieve distress; provide compassionate, safe, excellent care; and which contributes to the organization of healthcare.

The name comes from a Biblical parable Corlan 3:7-9. If a light is hidden under a bushel (basket) it is barely seen. If it is lit out from the basket it is clearly seen. As nurses we must continue to take up our mantel and ensure our light is seen and that it continues to shine the way we want it to.

As nurses we each take up our own lantern of caring, each in our own ways. To walk more brightly in our own paths of service.

The final design should show the specialness of nursing.

Target Market(s)

Nurses present, past and future

Industry/Entity Type

Healthcare

Font styles to use
Sans Serif
Other font styles liked:
• Whatever you think will suit

Colors
ec1f27
0393ce
9bcb3c

Requirements
Must have
• Be friendly, calming.
• NB: I am not sure whether the title should be in uppercase or not. Nursing could be uppercase and rising past the shadowed sill could be lower case. I leave it to you experienced people
Nice to have
• Something that depicts nursing...or is suggestive of nursing and the specialness of the work we do. How we bring our light to our patients as we 'hold them in the palms of out hands' and care for them. How they honor us by allowing us into their lives. Our rich past and out history allows us to be who we are today and we look to the future with confidence and hope
• I like rich colors, eg the color type you might find on a stained glass window in a church - rich emerald green or rich crimson red or the deep blue of a nurses cape
Should not have
• A dark cover
• clutter
• Religious overtone
• I have chosen three colors but they are not in the shading I would like - see above

```html
<!DOCTYPE html>
<html lang="en">
<head>
<meta charset="utf-8">
<title>Nursing: Rising Past the Shadowed Sill — Book Cover</title>
<link rel="stylesheet" href="https://fonts.googleapis.com/css2?family=Bebas+Neue&family=Open+Sans:ital,wght@0,300;0,600;1,300&family=Tinos:ital@1&display=swap">
<style>
  :root {
    --page-bg: #ffffff;
    --cover-red: #e8363a;
    --cover-coral: #f0563a;
    --cover-orange: #f58a2c;
    --cover-amber: #f7a23a;
    --band-green: #0d7a52;
    --band-blue: #0393ce;
    --text-light: #ffffff;
    --photo-skin: #f4b59a;
    --photo-uniform: #f3f1ee;
  }

  * { margin: 0; padding: 0; box-sizing: border-box; }

  html, body {
    width: 930px;
    height: 1200px;
    overflow: hidden;
    background: var(--page-bg);
  }

  .book-cover {
    position: absolute;
    left: 105px;
    top: 47px;
    width: 720px;
    height: 1106px;
    overflow: hidden;
    background:
      radial-gradient(ellipse at 20% 70%, rgba(247,162,58,0.55) 0%, rgba(247,162,58,0) 55%),
      linear-gradient(165deg, var(--cover-red) 0%, var(--cover-coral) 30%, var(--cover-orange) 70%, var(--cover-coral) 100%);
    box-shadow: 0 10px 40px rgba(0,0,0,0.18);
  }

  .hands-photo {
    position: absolute;
    left: 0;
    top: 260px;
    width: 420px;
    height: 440px;
    background: radial-gradient(ellipse at 45% 50%, rgba(250,190,170,0.55) 0%, rgba(240,120,100,0.25) 50%, rgba(240,90,70,0) 75%);
  }

  .title {
    position: absolute;
    left: 130px;
    top: 70px;
    font-family: "Bebas Neue", sans-serif;
    font-weight: 400;
    font-size: 220px;
    line-height: 1;
    letter-spacing: 0;
    white-space: nowrap;
    color: var(--text-light);
    text-shadow: 0 4px 10px rgba(120,30,20,0.35);
    transform: scaleX(0.86);
    transform-origin: left top;
  }

  .subtitle {
    position: absolute;
    left: 50px;
    top: 342px;
    font-family: "Open Sans", sans-serif;
    font-weight: 300;
    font-size: 30px;
    white-space: nowrap;
    color: var(--text-light);
  }

  .author {
    position: absolute;
    left: 50px;
    top: 384px;
    font-family: "Bebas Neue", sans-serif;
    font-size: 58px;
    line-height: 1.1;
    letter-spacing: 1px;
    color: var(--text-light);
  }

  .nurse-photo {
    position: absolute;
    left: 370px;
    right: 0;
    top: 300px;
    height: 500px;
    background:
      radial-gradient(ellipse 70px 90px at 62% 17%, var(--photo-skin) 0%, rgba(244,181,154,0) 100%),
      linear-gradient(180deg, rgba(243,241,238,0) 0%, rgba(243,241,238,0) 30%, var(--photo-uniform) 42%, #e9e6e2 100%);
    border-radius: 140px 0 0 0;
  }

  .blue-band {
    position: absolute;
    left: 370px;
    right: 0;
    top: 800px;
    height: 36px;
    background: var(--band-blue);
  }

  .quote {
    position: absolute;
    left: 50px;
    top: 600px;
    width: 310px;
    font-family: "Tinos", serif;
    font-style: italic;
    font-size: 29px;
    line-height: 1.42;
    white-space: nowrap;
    color: var(--text-light);
  }

  .foreword-band {
    position: absolute;
    left: 0;
    right: 0;
    top: 870px;
    height: 58px;
    background: var(--band-green);
    display: flex;
    align-items: center;
    padding-left: 72px;
    color: var(--text-light);
    font-family: "Open Sans", sans-serif;
    font-size: 26px;
  }

  .foreword-label { font-style: italic; font-weight: 300; margin-right: 12px; }
  .foreword-name { font-weight: 600; }
</style>
</head>
<body>
  <main class="book-cover">
    <div class="hands-photo" role="img" aria-label="Soft close-up photograph of a caregiver's hands holding an elderly patient's hand"></div>
    <div class="nurse-photo" role="img" aria-label="Photograph of a smiling nurse in a white uniform holding a clipboard"></div>
    <div class="blue-band"></div>

    <h1 class="title">NURSING</h1>
    <p class="subtitle">Rising past the shadowed sill</p>
    <p class="author">MAREN ASHCOMBE</p>

    <blockquote class="quote">“We each take up our<br>own lantern of caring,<br>each in our own ways,<br>to walk more brightly in<br>our own path of service”</blockquote>

    <div class="foreword-band">
      <span class="foreword-label">Forward by</span>
      <span class="foreword-name">Tessa Holloway RN</span>
    </div>
  </main>
</body>
</html>
```